Newspaper Ad for Cool Hawaiian PPE Company

We need an incredible ad for our local newspaper to tell everyone about BreezeGuard.net. We want a beautiful ad that is sophisticated with a local flair. Less is more. Clean. Stands out. We are safely shipping masks and PPE to our local community. Everyone has access to the supplies they need to keep them and their loved ones safe during the pandemic. Make it really pop.

Target Market(s)

Community members

Requirements
Must have
• Half Page:

Specs 9.7” x 10” column inches for the half page. Minimum 300 dpi, jpeg is fine.

```html
<!DOCTYPE html>
<html lang="en">
<head>
<meta charset="utf-8">
<title>BreezeGuard.net – Newspaper Ad</title>
<link href="https://fonts.googleapis.com/css2?family=Roboto+Condensed:ital,wght@0,400;1,300;1,700&display=swap" rel="stylesheet">
<style>
  :root {
    --paper: #ffffff;
    --ocean: #24708e;
    --leaf: #1f8f3f;
    --ink-light: #ffffff;
    --brand-grey: #6b6b6b;
  }
  * { margin: 0; padding: 0; box-sizing: border-box; }
  html, body {
    width: 1163px;
    height: 1200px;
    overflow: hidden;
    background: var(--paper);
  }
  .ad {
    position: relative;
    width: 1163px;
    height: 1200px;
    background: var(--paper);
    font-family: "Roboto Condensed", Arial, sans-serif;
  }
  .brand {
    position: absolute;
    left: 89px;
    top: 110px;
    width: 300px;
    display: flex;
    align-items: center;
    justify-content: center;
    gap: 12px;
  }
  .brand-dot {
    width: 26px;
    height: 26px;
    border-radius: 50%;
    background: var(--leaf);
  }
  .brand-name {
    font-weight: 400;
    font-size: 46px;
    color: var(--brand-grey);
    letter-spacing: -0.5px;
  }
  .tagline {
    position: absolute;
    left: 39px;
    top: 324px;
    width: 400px;
    text-align: center;
    font-style: italic;
    font-weight: 300;
    font-size: 34px;
    line-height: 49px;
    color: var(--leaf);
  }
  .band-left {
    position: absolute;
    left: 0;
    top: 577px;
    width: 520px;
    height: 623px;
    background: var(--ocean);
  }
  .band-bottom {
    position: absolute;
    left: 0;
    top: 1055px;
    width: 1163px;
    height: 145px;
    background: var(--ocean);
  }
  .photo {
    position: absolute;
    left: 519px;
    top: 109px;
    width: 644px;
    height: 946px;
    background: linear-gradient(180deg, #ece8e2 0%, #efece8 30%, #b8b3b0 55%, #c96a8a 78%, #e0a34a 100%);
  }
  .frame-green {
    position: absolute;
    left: 483px;
    top: 71px;
    width: 594px;
    height: 400px;
    border-top: 5px solid var(--leaf);
    border-left: 5px solid var(--leaf);
  }
  .frame-white {
    position: absolute;
    left: 483px;
    top: 674px;
    width: 438px;
    height: 425px;
    border-bottom: 5px solid var(--ink-light);
    border-left: 5px solid var(--ink-light);
  }
  .headline {
    position: absolute;
    left: 0;
    top: 0;
    width: 480px;
    height: 1200px;
  }
  .headline span {
    position: absolute;
    left: 0;
    width: 480px;
    text-align: center;
    font-style: italic;
    font-weight: 700;
    line-height: 1;
    color: var(--ink-light);
    white-space: nowrap;
  }
  .line-keep    { top: 648px;  font-size: 64px; }
  .line-and     { top: 707px;  font-size: 50px; }
  .line-loved   { top: 743px;  font-size: 86px; }
  .line-ones    { top: 807px;  font-size: 86px; }
  .line-safe    { top: 864px;  font-size: 134px; }
  .line-during  { top: 994px;  font-size: 50px; }
  .line-pandemic{ top: 1028px; font-size: 86px; }
  .web {
    position: absolute;
    left: 937px;
    top: 1079px;
    font-size: 26px;
    font-weight: 400;
    color: var(--ink-light);
  }
</style>
</head>
<body>
  <main class="ad">
    <div class="brand">
      <span class="brand-dot"></span>
      <span class="brand-name">BreezeGuard.net</span>
    </div>

    <p class="tagline">WE ARE SAFELY<br>SHIPPING MASKS<br>AND PPE TO OUR<br>LOCAL COMMUNITY</p>

    <div class="band-left"></div>
    <div class="band-bottom"></div>

    <div class="photo" role="img" aria-label="Photo of a young girl in a face mask at a farmers market, holding a dragon fruit beside a pile of yellow fruit"></div>

    <div class="frame-green"></div>
    <div class="frame-white"></div>

    <h1 class="headline">
      <span class="line-keep">KEEP THEM</span>
      <span class="line-and">AND THEIR</span>
      <span class="line-loved">LOVED</span>
      <span class="line-ones">ONES</span>
      <span class="line-safe">SAFE</span>
      <span class="line-during">DURING THE</span>
      <span class="line-pandemic">PANDEMIC</span>
    </h1>

    <p class="web">BreezeGuard.net</p>
  </main>
</body>
</html>
```